Business Cards

We were billed for this because the project timed out. Please give me another designed to open this back up. I was not happy with the last designs (that I was charged for).
we are also using the logo with Clear Water Care Season After Season
Also want to utilize Where Healthy Water is our Commitment.

Contact Information for Business Card

Marlowe Stone Group Inc

```html
<!DOCTYPE html>
<html lang="en">
<head>
<meta charset="utf-8">
<title>Marlowe Stone Group – Business Cards</title>
<link href="https://fonts.googleapis.com/css2?family=Michroma&family=Montserrat:wght@400;500;700&display=swap" rel="stylesheet">
<style>
  :root {
    --stage: #dedede;
    --card-white: #ffffff;
    --brand-blue: #1b6fc4;
    --brand-light: #3a9be0;
    --brand-deep: #0d4f99;
    --ink: #2b2b2b;
    --ink-soft: #444444;
    --edge: #3c9ee6;
  }
  * { margin: 0; padding: 0; box-sizing: border-box; }
  html, body { width: 1200px; height: 794px; overflow: hidden; background: var(--stage); }
  .stage { position: relative; width: 1200px; height: 794px; }

  .card {
    position: absolute;
    width: 500px;
    height: 286px;
    border-radius: 3px;
    box-shadow: 0 3px 0 var(--edge), 0 10px 22px rgba(0,0,0,0.12);
    overflow: hidden;
  }

  /* Back of card */
  .card-back { left: 110px; top: 110px; background: var(--brand-blue); }
  .card-back .pattern-field {
    position: absolute; inset: 0;
    background: linear-gradient(200deg, var(--brand-light) 0%, var(--brand-blue) 45%, var(--brand-deep) 100%);
  }
  .card-back .back-name {
    position: absolute; right: 34px; top: 128px;
    display: flex; align-items: center; gap: 8px;
    font-family: "Montserrat", sans-serif; font-weight: 700;
    font-size: 15px; letter-spacing: 1px; color: var(--card-white);
  }
  .back-name .mark-square { width: 12px; height: 12px; background: var(--card-white); }

  /* Front of card */
  .card-front { left: 590px; top: 398px; background: var(--card-white); }
  .front-brand {
    position: absolute; left: 36px; top: 0; bottom: 0;
    display: flex; flex-direction: column; justify-content: center; gap: 2px;
    font-family: "Montserrat", sans-serif; font-weight: 700;
    font-size: 22px; line-height: 1.05; color: var(--brand-blue);
  }
  .front-brand .mark-square { width: 16px; height: 16px; background: var(--brand-blue); margin-bottom: 10px; }

  .front-info {
    position: absolute; right: 28px; top: 26px;
    text-align: right;
    font-family: "Montserrat", sans-serif;
  }
  .company {
    font-family: "Michroma", sans-serif;
    font-size: 15px; letter-spacing: 0.5px; color: var(--ink);
  }
  .tagline {
    font-size: 6.6px; letter-spacing: 1.6px; color: var(--ink-soft);
    text-transform: uppercase; margin-top: 2px;
  }
  .person { margin-top: 22px; font-size: 19px; font-weight: 500; letter-spacing: 0.2px; }
  .person .first { color: var(--brand-light); }
  .person .last { color: var(--brand-deep); }
  .role { font-size: 11px; color: var(--ink-soft); margin-top: 1px; }
  .address { margin-top: 12px; font-size: 11px; line-height: 1.4; color: var(--ink); }
  .contacts { margin-top: 10px; font-size: 11px; line-height: 1.5; color: var(--ink); list-style: none; }
  .contacts li { display: flex; justify-content: flex-end; align-items: center; gap: 5px; }
  .contacts .accent { color: var(--brand-blue); }
  .contacts svg { width: 9px; height: 9px; flex: none; }
</style>
</head>
<body>
<main class="stage">

  <section class="card card-back">
    <div class="pattern-field" role="img" aria-label="Repeating embossed brand mark pattern in tones of blue"></div>
    <div class="back-name"><span class="mark-square"></span>MARLOWE STONE GROUP</div>
  </section>

  <section class="card card-front">
    <div class="front-brand">
      <span class="mark-square"></span>
      <span>MARLOWE</span>
      <span>STONE</span>
      <span>GROUP</span>
    </div>

    <div class="front-info">
      <p class="company">MARLOWE STONE GROUP</p>
      <p class="tagline">Clear Water Care Season After Season</p>

      <p class="person"><span class="first">DANA</span> <span class="last">WHITFIELD</span></p>
      <p class="role">Managing Director</p>

      <p class="address">418 Cedar Bend Road<br>Salem, OR 97301</p>

      <ul class="contacts">
        <li>+945-555-0142
          <svg viewBox="0 0 10 10"><path d="M2 1 L4 1 L4.6 3 L3.5 4 Q4.5 6 6 6.5 L7 5.4 L9 6 L9 8 Q8.5 9 7 9 Q1 8 1 2.5 Q1 1 2 1 Z" fill="var(--brand-blue)"/></svg>
        </li>
        <li>info@marlowestonegroup.com
          <svg viewBox="0 0 10 10"><rect x="1" y="2.5" width="8" height="5.5" fill="none" stroke="var(--brand-blue)" stroke-width="1"/><path d="M1 2.5 L5 5.5 L9 2.5" fill="none" stroke="var(--brand-blue)" stroke-width="1"/></svg>
        </li>
        <li><span>www.<span class="accent">marlowestonegroup</span>.com</span>
          <svg viewBox="0 0 10 10"><circle cx="5" cy="5" r="4" fill="var(--brand-blue)"/><path d="M1 5 H9 M5 1 Q2.5 5 5 9 M5 1 Q7.5 5 5 9" fill="none" stroke="#fff" stroke-width="0.7"/></svg>
        </li>
      </ul>
    </div>
  </section>

</main>
</body>
</html>
```